Webdesign für Kleingruppenreisen in die Südsteiermark
Zielgruppe
Wir sind ein Start-Up Unternehmen, das als Kleingruppenreisen in die Südsteiermark veranstaltet; der Schwerpunkt liegt auf dem Kulinarischen. Zielgruppe sind Geschäftsleute, die diese Kurzreisen (Do-So) für Marketingzwecke oder als Mitarbeiterbonus (oder auch privat) nutzen möchten.
Aufgabenstellung
Die Homepage soll eine Online-Shop Möglichkeit bieten, in der die Reise (bisher gibt es nur einen Ablauf) gebucht werden kann. Optisch sollte sie sich an das bereits von Ihnen erstellte Logo anlehnen und möglichst ansprechende Fotos von der Südsteiermark, Graz, Leoben usw. enthalten. (Siehe die beiden Flyer und das Logo)
Wir haben inzwischen Bildfreigaben von Mirtler und dem Tourismusverband Hollerau erhalten und können auch eigene Bilder zur Verfügung stellen. Bitte kontaktieren Sie uns dafür, wenn nötig.

```html
<!DOCTYPE html>
<html lang="de">
<head>
<meta charset="utf-8">
<title>Feinkostfahrt – Kleingruppenreisen in die Steiermark</title>
<link href="https://fonts.googleapis.com/css2?family=Lato:ital,wght@0,400;0,700;0,900;1,400;1,900&family=Montserrat:wght@400&display=swap" rel="stylesheet">
<style>
:root{
  --cream:#fdf3ea;
  --card:#fdf3ea;
  --text:#2f2f2f;
  --green:#5aa76a;
  --aqua:#86d3d9;
  --panel:rgba(58,100,80,.72);
  --footer:#2b2b2b;
  --teal:#5e8f8f;
  --accent:#7fd0d6;
  --brand:#b3241f;
}
*{margin:0;padding:0;box-sizing:border-box}
html,body{width:739px;height:1200px;overflow:hidden}
body{font-family:"Lato",sans-serif;color:var(--text);background:#fff;position:relative}
.site-header{position:absolute;top:0;left:0;width:739px;height:79px;background:var(--cream)}
.nav-link{position:absolute;top:55px;font-size:9.5px;color:#333}
.brand{position:absolute;left:312px;top:38px;width:118px;text-align:center}
.brand-name{font-size:16px;font-weight:900;color:var(--brand);display:flex;align-items:center;justify-content:center;gap:4px}
.brand-name .dot{width:7px;height:7px;border-radius:50%;background:var(--brand)}
.brand-tag{font-size:5px;color:#333;margin-top:1px}
.photo{position:absolute;left:0;width:739px}
.photo-vineyard{top:85px;height:277px;background:linear-gradient(160deg,#3c4a14 0%,#8b7a22 35%,#e7c870 55%,#6f7a35 75%,#34401a 100%)}
.photo-wine{top:558px;height:277px;background:linear-gradient(180deg,#8a5a3a 0%,#7d9fb0 35%,#6f9a55 65%,#3f6d2a 100%)}
.callout{position:absolute;background:var(--panel);box-shadow:2px 2px 4px rgba(0,0,0,.3);text-align:center;color:#fff}
.callout h2{font-weight:900;font-style:italic;font-size:28px;line-height:29px}
.cta{display:inline-block;background:var(--aqua);color:#fff;font-style:italic;font-size:16px;border-radius:8px;padding:6px 25px}
.callout-hero{left:351px;top:146px;width:281px;height:115px;padding-top:6px}
.callout-hero .cta{margin-top:8px;width:135px;padding:6px 0}
.callout-contact{left:55px;top:665px;width:282px;height:116px;padding-top:9px}
.callout-contact h2{font-size:23px;line-height:28px}
.callout-contact .cta{margin-top:7px;width:162px;padding:6px 0}
.card{position:absolute;width:153px;height:169px;background:var(--card);box-shadow:0 1px 3px rgba(0,0,0,.25);font-size:7.8px;line-height:13.4px;padding:48px 4px 0 6px;white-space:nowrap;overflow:hidden}
.card .icon{position:absolute;left:58px;top:6px;width:37px;height:37px;border-radius:50%;background:#fff;box-shadow:0 1px 3px rgba(0,0,0,.25);display:flex;align-items:center;justify-content:center}
.card ul{list-style:none}
.card li{display:flex;align-items:center;gap:4px;margin-top:4px}
.card p+p{margin-top:3px}
.row1{top:377px}.row2{top:850px}
.c1{left:101px}.c2{left:293px}.c3{left:486px}
.site-footer{position:absolute;top:1035px;left:0;width:739px;height:165px;background:var(--footer);color:#fff}
.newsletter{position:absolute;left:101px;top:17px;width:537px;height:33px;background:var(--teal);border-radius:5px}
.nl-field{position:absolute;left:3px;top:5px;width:143px;height:23px;background:#fff;border-radius:2px;display:flex}
.nl-field .mail{width:31px;border-right:1px solid #ccc;display:flex;align-items:center;justify-content:center}
.nl-field span{font-size:7px;color:#999;padding:8px 0 0 17px}
.nl-text{position:absolute;left:177px;top:6px;font-size:7px;line-height:9px}
.nl-text strong{font-size:11px;line-height:13px;display:block}
.nl-text small{font-size:6.6px;line-height:8px;display:block;white-space:nowrap}
.foot-col{position:absolute;top:67px;font-family:"Montserrat",sans-serif;font-size:8.5px;line-height:13.4px}
.foot-col h3{font-family:"Lato",sans-serif;font-size:8.5px;color:var(--accent);font-weight:700;margin-bottom:3px}
.foot-col.phone{left:101px;font-family:"Lato",sans-serif}
.foot-col.service{left:276px}
.foot-col.info{left:460px}
</style>
</head>
<body>
<header class="site-header">
  <a class="nav-link" style="left:160px">Start</a>
  <a class="nav-link" style="left:216px">Reise buchen</a>
  <div class="brand">
    <div class="brand-name"><span class="dot"></span>Feinkostfahrt</div>
    <div class="brand-tag">Reisen für Feinschmecker in die Steiermark</div>
  </div>
  <a class="nav-link" style="left:466px">Kontakt</a>
  <a class="nav-link" style="left:534px">Impressum</a>
</header>

<div class="photo photo-vineyard" role="img" aria-label="Weinberge der Südsteiermark im Sonnenuntergang"></div>
<div class="callout callout-hero">
  <h2>Haben Sie Geschmack am Besonderen?</h2>
  <span class="cta">Reise buchen</span>
</div>

<section class="card row1 c1" style="padding-left:14px">
  <div class="icon"><svg width="18" height="20" viewBox="0 0 18 20"><path d="M1 4h6l-1 5a2 2 0 0 1-4 0z M4 11v6 M2 17h4" stroke="#5aa76a" stroke-width="1.5" fill="none"/><rect x="10" y="6" width="6" height="13" rx="1" fill="#5aa76a"/><rect x="12" y="1" width="2" height="6" fill="#5aa76a"/></svg></div>
  <p>Lieben Sie...</p>
  <ul>
    <li><svg width="6" height="8" viewBox="0 0 6 8"><path d="M3 0a3 3 0 0 1 3 3c0 2-3 5-3 5S0 5 0 3a3 3 0 0 1 3-3z" fill="#5aa76a"/></svg>gutes Essen?</li>
    <li><svg width="6" height="8" viewBox="0 0 6 8"><path d="M3 0a3 3 0 0 1 3 3c0 2-3 5-3 5S0 5 0 3a3 3 0 0 1 3-3z" fill="#5aa76a"/></svg>hervorragendes Bier?</li>
    <li><svg width="6" height="8" viewBox="0 0 6 8"><path d="M3 0a3 3 0 0 1 3 3c0 2-3 5-3 5S0 5 0 3a3 3 0 0 1 3-3z" fill="#5aa76a"/></svg>exquisiten Wein?</li>
    <li><svg width="6" height="8" viewBox="0 0 6 8"><path d="M3 0a3 3 0 0 1 3 3c0 2-3 5-3 5S0 5 0 3a3 3 0 0 1 3-3z" fill="#5aa76a"/></svg>kulinarische Spezialitäten?</li>
    <li><svg width="6" height="8" viewBox="0 0 6 8"><path d="M3 0a3 3 0 0 1 3 3c0 2-3 5-3 5S0 5 0 3a3 3 0 0 1 3-3z" fill="#5aa76a"/></svg>und gastfreundliche Menschen?</li>
    <li><svg width="6" height="8" viewBox="0 0 6 8"><path d="M3 0a3 3 0 0 1 3 3c0 2-3 5-3 5S0 5 0 3a3 3 0 0 1 3-3z" fill="#5aa76a"/></svg>wunderschöne Landschaften?</li>
  </ul>
</section>
<section class="card row1 c2" style="padding-left:5px">
  <div class="icon"><svg width="26" height="18" viewBox="0 0 26 18"><ellipse cx="13" cy="9" rx="4" ry="8" fill="#5aa76a"/><ellipse cx="6" cy="11" rx="3.5" ry="6" fill="#5aa76a" transform="rotate(-25 6 11)"/><ellipse cx="20" cy="11" rx="3.5" ry="6" fill="#5aa76a" transform="rotate(25 20 11)"/></svg></div>
  <p>Wir glauben, dass unsere Reisen<br>hervorragende Möglichkeiten zum<br>Entspannen und Genießen bieten<br>und sich deshalb besonders gut als<br>„Schmankerl” für umsatzstarke Kunden,<br>erfolgreiche Mitarbeiter oder einfach<br>für Sie selbst und Ihre Freunde eignen.</p>
</section>
<section class="card row1 c3" style="padding-left:7px">
  <div class="icon"><svg width="28" height="16" viewBox="0 0 28 16"><path d="M2 8l24-3c2 0 2 3 0 3L2 10z M12 7l-5-7h3l8 7z M12 9l-4 7h3l7-7z M2 9l-2-5h2l3 5z" fill="#5aa76a"/></svg></div>
  <p>Lassen Sie das hektische Berlin und das<br>flache Land für ein paar Tage hinter<br>sich!<br>Die südlichen Ausläufer der Alpen und<br>die sogenannte „steirische Toskana”<br>sind nur 90 Minuten Direktflug<br>entfernt.</p>
</section>

<div class="photo photo-wine" role="img" aria-label="Weißwein wird im Freien vor grüner Landschaft in zwei Gläser eingeschenkt"></div>
<div class="callout callout-contact">
  <h2>Sind Sie auf den<br>Geschmack gekommen?</h2>
  <span class="cta">kontaktieren Sie uns</span>
</div>

<section class="card row2 c1" style="padding-left:7px">
  <div class="icon"><svg width="14" height="20" viewBox="0 0 14 20"><rect x="2" y="1" width="2" height="18" fill="#5aa76a"/><path d="M4 2l9 3-9 4z" fill="#5aa76a"/></svg></div>
  <p>Lernen Sie Leoben, die Hauptstadt des<br>Mirtler-Bieres kennen und erfahren Sie<br>im Mirtleum die Geschichte dieses<br>weltbekannten Gebräus.</p>
</section>
<section class="card row2 c2" style="padding-left:4px">
  <div class="icon"><svg width="26" height="26" viewBox="0 0 26 26"><circle cx="13" cy="13" r="6" fill="#5aa76a"/><g fill="#5aa76a"><path d="M13 0l2 4h-4z"/><path d="M13 26l2-4h-4z"/><path d="M0 13l4 2v-4z"/><path d="M26 13l-4 2v-4z"/><path d="M4 4l4 1-3 3z"/><path d="M22 22l-4-1 3-3z"/><path d="M22 4l-1 4-3-3z"/><path d="M4 22l1-4 3 3z"/></g></svg></div>
  <p>Entdecken Sie Graz, die abwechslungs-<br>reiche Landeshauptstadt und Kultur-<br>hauptstadt 2003, mit ihren vielfältigen<br>kulturellen Angeboten, den charmanten<br><span style="letter-spacing:-.15px">Gassen und atemberaubenden Ausblicken.</span></p>
  <p>Genießen Sie die südlichere Sonne und<br>kosten Sie die ausgezeichneten Weine<br>der Winzer in der Buschenschank.</p>
</section>
<section class="card row2 c3" style="padding-left:5px">
  <div class="icon"><svg width="24" height="18" viewBox="0 0 24 18"><rect x="3" y="1" width="18" height="7" rx="1" fill="#5aa76a"/><rect x="6" y="3" width="12" height="3" fill="#fff"/><rect x="1" y="9" width="22" height="8" rx="1" fill="#5aa76a"/></svg></div>
  <p>Während unser Exklusiv Transfer Sie zu<br>den Sehenswürdigkeiten bringt, lüftet<br>unser steirischer Reiseleiter für Sie die<br>Geheimnisse seines Heimatlandes, des<br><span style="letter-spacing:-.1px">„grünen Herzens Österreichs“ und führt</span><br>Sie in erstklassige Restaurants.</p>
  <p>Sie wohnen in ausgesuchten Hotels in<br>zentraler Lage.</p>
</section>

<footer class="site-footer">
  <div class="newsletter">
    <div class="nl-field">
      <div class="mail"><svg width="17" height="12" viewBox="0 0 17 12"><rect x="0.5" y="0.5" width="16" height="11" fill="#7fd0d6" stroke="#5e8f8f"/><path d="M0.5 0.5l8 6 8-6" stroke="#fff" fill="none"/></svg></div>
      <span>Ihre E-Mail Adresse</span>
    </div>
    <div class="nl-text">
      <strong>Newsletter</strong>
      <small>Abonnieren Sie unseren kostenlosen Newsletter und verpasse keine Neuigkeiten</small>
    </div>
  </div>
  <div class="foot-col phone">
    <h3>Telefon</h3>
    <p>XXXXXXXXXX<br>Montag bis Freitag<br>von XX bis XX Uhr</p>
  </div>
  <div class="foot-col service">
    <h3>Service</h3>
    <p>Kontakt<br>&nbsp;Zahlungsbedingungen<br>AGB<br>Widerrufsrecht<br>Widerrufsformular<br>Partnerprogramm</p>
  </div>
  <div class="foot-col info">
    <h3>Informationen</h3>
    <p>Über uns<br>Datenschutz<br>Impressum<br>Newsletter</p>
  </div>
</footer>
</body>
</html>
```